Halvard Compute - Direct Mailer / Flyer

We are excited to announce the launch of our new company, Halvard Compute, a premier cohosting facility and data center dedicated to Cryptocurrency Miners. Our website, https://halvardcompute.example, provides detailed information about our offerings and showcases the innovative design schemes for the entire project.

Halvard Compute stands out in the industry by offering both GPU Hosting and ASIC Hosting services in our state-of-the-art facility, equipped with an impressive 17 Megawatts of available power. What sets us apart is our unique billing system based on actual metered power usage. We charge $0.08 for ASIC miners and $0.09 for GPU miners, ensuring cost-effectiveness and transparency for our clients.

Our commitment to excellence is evident in our use of cutting-edge technology, top-notch facilities, and strategic partnerships. These elements come together to deliver exceptional solutions tailored for real-world applications in the cryptocurrency space.

As part of our promotional efforts, we are developing a direct mailer/flyer to introduce Halvard Compute to a wider audience. This promotional material will also serve as a handout at events, to potential customers, and more. We welcome creative ideas and suggestions to maximize the versatility of this design and reach diverse target audiences effectively.

For a comprehensive overview of our services and to explore our design concepts, please visit https://halvardcompute.example. Halvard Compute is poised to revolutionize the mining industry, and we look forward to partnering with you for success in the digital currency era.

```html
<!DOCTYPE html>
<html lang="en">
<head>
<meta charset="utf-8">
<title>Halvard Compute – Flyer Front and Back</title>
<link href="https://fonts.googleapis.com/css2?family=Space+Grotesk:wght@400;500;600;700&display=swap" rel="stylesheet">
<style>
:root{
  --stage:#9c9c9c;
  --blue:#3a5bff;
  --blue-deep:#2f4ee6;
  --green:#0e8a2a;
  --magenta:#c0189a;
  --ink:#0d0d0d;
  --white:#ffffff;
  --grey-band:#e8e8ea;
  --mission-bg:#e6e9f7;
  --role-bg:#e4efe7;
  --values-bg:#f1e4ef;
  --body-ink:#3a3a44;
  --font:"Space Grotesk", sans-serif;
}
*{box-sizing:border-box;margin:0;padding:0}
html,body{width:1200px;height:800px;overflow:hidden}
body{background:var(--stage);font-family:var(--font);position:relative;color:var(--ink)}
.side-label{position:absolute;top:30px;width:519px;text-align:center;color:var(--white);font-weight:700;font-size:21px;letter-spacing:12px}
.flyer{position:absolute;top:64px;width:519px;height:671px;background:var(--white);overflow:hidden}
.flyer--front{left:66px}
.flyer--back{left:622px}
.abs{position:absolute}

/* brand */
.brand{display:flex;align-items:center;gap:6px;font-weight:700;font-size:19px;color:var(--ink);letter-spacing:.3px;white-space:nowrap}
.brand__square{width:20px;height:20px;background:var(--ink);border-radius:2px}

/* price badges */
.price{position:absolute;top:30px;height:30px;width:118px;border-radius:6px;color:var(--white);display:flex;align-items:center;padding-left:8px;gap:3px}
.price--asic{left:258px;background:var(--blue)}
.price--gpu{left:380px;background:var(--green)}
.price__amount{font-size:21px;font-weight:600;letter-spacing:-.5px}
.price__amount sup{font-size:10px;vertical-align:8px}
.price__note{font-size:8.5px;line-height:1;font-weight:500}

/* hero */
.hero__bar{left:0;top:82px;width:6px;height:145px;background:var(--green)}
.hero__title{left:37px;top:80px;font-size:33px;font-weight:700;line-height:34px;letter-spacing:-.4px}
.hero__title .accent{color:var(--blue)}
.hero__sub{left:38px;top:189px;font-size:11px;line-height:13.5px;color:#222;width:170px}
.hero__art{left:240px;top:62px;width:272px;height:178px;border-radius:90px 90px 8px 8px;background:radial-gradient(circle at 55% 45%,#dcebff 0%,#eef4ff 55%,#ffffff 100%)}
.hero__floor{left:248px;top:237px;width:256px;height:1px;background:#333}

/* hosting band */
.hosting{left:0;top:259px;width:519px;height:217px;background:var(--blue);color:var(--white)}
.hosting__title{position:absolute;top:14px;width:100%;text-align:center;font-size:19px;font-weight:600}
.feature{position:absolute;width:140px}
.feature__icon{position:absolute;left:-24px;top:-2px;width:16px;height:18px}
.feature__name{font-size:9.5px;font-weight:600;margin-bottom:5px;white-space:nowrap}
.feature__text{font-size:7.6px;line-height:9.4px;opacity:.95}

/* commitment band */
.commit{left:0;top:476px;width:519px;height:156px;background:var(--grey-band)}
.commit__text{position:absolute;left:35px;top:21px;font-size:13.5px;font-weight:600;line-height:17px;width:120px}
.commit__svg{position:absolute;left:0;top:0}
.hex-label{position:absolute;width:100px;text-align:center;color:var(--white);font-size:10px;font-weight:600;line-height:12px}

/* footer */
.footer{left:0;bottom:0;width:519px;height:39px;background:#000;color:var(--white);display:flex;justify-content:center;align-items:center;gap:18px;font-size:11.5px}
.footer__item{display:flex;align-items:center;gap:5px}

/* back header */
.about{left:0;top:0;width:519px;height:144px;background:var(--blue)}
.about__pointer{left:56px;top:143px;width:0;height:0;border-left:17px solid transparent;border-right:17px solid transparent;border-top:13px solid var(--blue)}
.about__title{left:41px;top:27px;font-size:29px;font-weight:700;line-height:30.5px;color:var(--white);letter-spacing:-.3px}
.about__text{left:280px;top:33px;width:218px;font-size:8px;line-height:10.2px;color:var(--white)}
.about__brand{left:280px;top:99px}

/* pillar cards */
.pillar{position:absolute;top:185px;width:148px;height:201px;border-radius:10px;overflow:hidden}
.pillar--mission{left:35px;background:var(--mission-bg)}
.pillar--role{left:189px;background:var(--role-bg)}
.pillar--values{left:345px;background:var(--values-bg)}
.pillar__tab{position:absolute;left:0;top:0;width:48px;height:45px;border-radius:10px 0 10px 0;display:flex;align-items:center;justify-content:center}
.pillar--mission .pillar__tab{background:var(--blue)}
.pillar--role .pillar__tab{background:var(--green)}
.pillar--values .pillar__tab{background:var(--magenta)}
.pillar__title{position:absolute;left:59px;top:17px;font-size:12px;font-weight:500}
.pillar--mission .pillar__title{color:var(--blue)}
.pillar--role .pillar__title{color:var(--green)}
.pillar--values .pillar__title{color:var(--magenta)}
.pillar__body{position:absolute;left:17px;top:57px;width:122px;font-size:7.2px;line-height:9.2px;color:var(--body-ink)}
.pillar__body p+p{margin-top:9px}

/* scalability */
.scale__art{left:36px;top:406px;width:219px;height:194px;border-radius:8px;background:linear-gradient(160deg,#f4f5f8 0%,#e4e9f6 55%,#c9d6ff 100%)}
.scale__title{left:283px;top:413px;font-size:20px;font-weight:600;line-height:25px}
.scale__text{left:284px;top:466px;width:190px;font-size:7.6px;line-height:9.2px;color:#333}
.perk{position:absolute;left:283px;width:172px;height:39px;border-radius:6px;color:var(--white);display:flex;align-items:center;gap:8px;padding-left:12px}
.perk--scale{top:501px;background:var(--blue)}
.perk--cost{top:543px;background:var(--green)}
.perk__name{font-size:9px;font-weight:600}
.perk__desc{font-size:7.2px}
</style>
</head>
<body>

<div class="side-label" style="left:66px">FRONT</div>
<div class="side-label" style="left:622px">BACK</div>

<!-- FRONT -->
<section class="flyer flyer--front">
  <div class="abs brand" style="left:38px;top:32px"><span class="brand__square"></span>HALVARD COMPUTE</div>

  <div class="price price--asic"><span class="price__amount"><sup>$</sup>0.08</span><span class="price__note">for<br>ASIC miners</span></div>
  <div class="price price--gpu"><span class="price__amount"><sup>$</sup>0.09</span><span class="price__note">for<br>GPU miners</span></div>

  <div class="abs hero__bar"></div>
  <h1 class="abs hero__title">Transform<br><span class="accent">Mining</span> With<br>Cohosting</h1>
  <p class="abs hero__sub">a premier cohosting facility and data center dedicated to Cryptocurrency Miners.</p>
  <div class="abs hero__art" role="img" aria-label="Illustration of a team working with data dashboards beside a stack of secured servers"></div>
  <div class="abs hero__floor"></div>

  <div class="abs hosting">
    <h2 class="hosting__title">Hosting Tailored To Your Needs</h2>

    <div class="feature" style="left:69px;top:54px">
      <svg class="feature__icon" viewBox="0 0 16 18" fill="none" stroke="#fff" stroke-width="1.3"><path d="M9 1 3 10h5l-2 7 7-10H8z"/></svg>
      <div class="feature__name">99.45% Uptime</div>
      <div class="feature__text">We boast an impressive uptime of 99.45% on average, ensuring consistent availability and reliability for users.</div>
    </div>
    <div class="feature" style="left:225px;top:54px">
      <svg class="feature__icon" viewBox="0 0 16 18" fill="none" stroke="#fff" stroke-width="1.3"><rect x="2" y="1" width="11" height="5"/><rect x="2" y="6" width="11" height="5"/><rect x="2" y="11" width="7" height="5"/><path d="M11 12h4v3l-2 2-2-2z"/></svg>
      <div class="feature__name">Advanced Security</div>
      <div class="feature__text">Employing advanced security measures for protection against potential threats and unauthorized access.</div>
    </div>
    <div class="feature" style="left:372px;top:54px">
      <svg class="feature__icon" viewBox="0 0 18 18" fill="none" stroke="#fff" stroke-width="1.3"><rect x="1" y="10" width="16" height="6"/><rect x="4" y="5" width="6" height="5"/><rect x="10" y="1" width="6" height="6"/></svg>
      <div class="feature__name">Large Facility Capacity</div>
      <div class="feature__text">Our 17MW facility capacity underscores the infrastructure's ability to accommodate high-energy demands.</div>
    </div>
    <div class="feature" style="left:69px;top:133px">
      <svg class="feature__icon" viewBox="0 0 18 18" fill="none" stroke="#fff" stroke-width="1.3"><path d="M3 10V8a6 6 0 0 1 12 0v2"/><rect x="1.5" y="9" width="3" height="5" rx="1"/><rect x="13.5" y="9" width="3" height="5" rx="1"/><path d="M15 14c0 2-3 3-5 3"/></svg>
      <div class="feature__name">Expert Support</div>
      <div class="feature__text">Benefit from expert support, ensuring assistance and guidance to optimize equipment and resolve issues effectively.</div>
    </div>
    <div class="feature" style="left:225px;top:133px">
      <svg class="feature__icon" viewBox="0 0 18 18" fill="none" stroke="#fff" stroke-width="1.3"><circle cx="9" cy="9" r="7.5"/><path d="M9 9l4-4"/><circle cx="9" cy="9" r="1.2"/></svg>
      <div class="feature__name">Metered Usage</div>
      <div class="feature__text">We exclusively bill you based on your usage, without exceptions! Leveraging state-of-the-art metering.</div>
    </div>
    <div class="feature" style="left:372px;top:133px">
      <svg class="feature__icon" viewBox="0 0 18 18" fill="none" stroke="#fff" stroke-width="1.3"><circle cx="12" cy="5" r="4"/><path d="M9 8 2 15l2 2 1-1-1-1 2-2 1 1 1-1-1-1 2-2"/></svg>
      <div class="feature__name">Direct Equipment Access</div>
      <div class="feature__text">Effectively command your operations with a comprehensive, full-spectrum control system - you got the keys.</div>
    </div>
  </div>

  <div class="abs commit">
    <svg class="commit__svg" width="519" height="156" viewBox="0 0 519 156">
      <path d="M35 98H152L168 130H238L262 98H290L310 130H360L380 98H406L426 130H476L488 98" fill="none" stroke="var(--blue)" stroke-width="1.2"/>
      <polygon points="176,24 230,24 257,71 230,118 176,118 149,71" fill="var(--blue)"/>
      <polygon points="293,24 347,24 374,71 347,118 293,118 266,71" fill="var(--blue)"/>
      <polygon points="412,24 466,24 493,71 466,118 412,118 385,71" fill="var(--blue)"/>
      <g fill="none" stroke="#fff" stroke-width="1.2">
        <circle cx="203" cy="44" r="8"/><circle cx="203" cy="44" r="3"/>
        <circle cx="316" cy="44" r="6"/><circle cx="327" cy="40" r="4"/><path d="M316 50v8"/>
        <path d="M428 46l7-5 7 4 7-4 7 5-7 6-7-4-7 4z"/>
      </g>
    </svg>
    <p class="commit__text">Our commitment to excellence is evident in our use of</p>
    <div class="hex-label" style="left:153px;top:64px">Cutting-edge<br>Technology</div>
    <div class="hex-label" style="left:270px;top:64px">Top-notch<br>Facilities</div>
    <div class="hex-label" style="left:389px;top:64px">Strategic<br>Partnerships</div>
  </div>

  <footer class="abs footer">
    <span class="footer__item"><svg width="12" height="12" viewBox="0 0 12 12" fill="none" stroke="#6f8cff" stroke-width="1.1"><path d="M2 1h3l1 3-2 1a7 7 0 0 0 3 3l1-2 3 1v3c-6 1-10-3-9-9z"/></svg>555-014-2290</span>
    <span class="footer__item"><svg width="12" height="12" viewBox="0 0 12 12" fill="none" stroke="#6f8cff" stroke-width="1"><circle cx="6" cy="6" r="5"/><ellipse cx="6" cy="6" rx="2.2" ry="5"/><path d="M1 6h10"/></svg>WWW.HALVARDCOMPUTE.EXAMPLE</span>
  </footer>
</section>

<!-- BACK -->
<section class="flyer flyer--back">
  <div class="abs about"></div>
  <div class="abs about__pointer"></div>
  <h2 class="abs about__title">Who We Are<br>And Why We’re<br>Doing This</h2>
  <p class="abs about__text">This venture is our passion, not just a business. We are deeply committed to Halvard Compute, driven by our belief in its transformative potential and our dedication to making a meaningful impact in the cryptocurrency industry.</p>
  <div class="abs brand about__brand"><span class="brand__square"></span>HALVARD COMPUTE</div>

  <article class="pillar pillar--mission">
    <div class="pillar__tab"><svg width="26" height="26" viewBox="0 0 26 26" fill="none" stroke="#fff" stroke-width="1.6"><circle cx="13" cy="13" r="11"/><path d="M5 8c4 1 5 4 3 7s1 5 3 6M17 3c-2 3 0 5 3 5s3 4 1 7"/></svg></div>
    <h3 class="pillar__title">Our Mission</h3>
    <div class="pillar__body">
      <p>At Halvard Compute, our mission is to empower cryptocurrency miners by providing transparent, efficient, and reliable cohosting solutions.</p>
      <p>We strive to optimize mining operations through innovative technology, fair pricing models, and exceptional customer support, fostering growth and sustainability in the cryptocurrency landscape.</p>
    </div>
  </article>
  <article class="pillar pillar--role">
    <div class="pillar__tab"><svg width="26" height="26" viewBox="0 0 26 26" fill="none" stroke="#fff" stroke-width="1.8"><path d="M13 2 22 7v12l-9 5-9-5V7z"/><path d="M9 16l7-7M9 10v6h6"/></svg></div>
    <h3 class="pillar__title">Our Role</h3>
    <div class="pillar__body">
      <p>At Halvard Compute, our role is to facilitate seamless and cost-effective cryptocurrency mining operations by offering transparent cohosting services tailored to meet the diverse needs of our clients.</p>
      <p>We aim to empower miners with reliable infrastructure, efficient resources, and dedicated support, enabling them to thrive.</p>
    </div>
  </article>
  <article class="pillar pillar--values">
    <div class="pillar__tab"><svg width="28" height="26" viewBox="0 0 28 26" fill="none" stroke="#fff" stroke-width="1.6"><circle cx="8" cy="6" r="3.5"/><circle cx="20" cy="6" r="3.5"/><circle cx="14" cy="14" r="3.5"/><path d="M2 16c0-3 3-5 6-5M26 16c0-3-3-5-6-5M8 25c0-4 3-6 6-6s6 2 6 6"/></svg></div>
    <h3 class="pillar__title">Our Values</h3>
    <div class="pillar__body">
      <p>At Halvard Compute, we uphold integrity, transparency, and innovation as our core values.</p>
      <p>We are committed to fostering trust, accountability, and sustainability in all our interactions. By prioritizing these values with our continuous improvement, we strive to be the trusted partner of choice for cryptocurrency miners.</p>
    </div>
  </article>

  <div class="abs scale__art" role="img" aria-label="Illustration of two businessmen climbing a large rising blue arrow in front of a city skyline"></div>
  <h2 class="abs scale__title">Unleash The Power<br>Of Scalability</h2>
  <p class="abs scale__text">Unlock the potential for limitless growth with our scalable solutions. No more roadblocks, no more time constraints.</p>

  <div class="perk perk--scale">
    <svg width="20" height="20" viewBox="0 0 20 20" fill="none" stroke="#fff" stroke-width="1.3"><rect x="1" y="9" width="10" height="10"/><rect x="4" y="12" width="4" height="4"/><rect x="11" y="1" width="7" height="7"/><path d="M11 12h4v4h-4"/></svg>
    <div><div class="perk__name">Scalability</div><div class="perk__desc">Easily scale your operations</div></div>
  </div>
  <div class="perk perk--cost">
    <svg width="20" height="20" viewBox="0 0 20 20" fill="none" stroke="#fff" stroke-width="1.3"><path d="M1 1v18h18"/><path d="M4 14l4-4 3 3 7-7M14 6h4v4"/></svg>
    <div><div class="perk__name">Cost Efficiency</div><div class="perk__desc">Pay only for the resources you use</div></div>
  </div>

  <footer class="abs footer">
    <span class="footer__item"><svg width="12" height="12" viewBox="0 0 12 12" fill="none" stroke="#6f8cff" stroke-width="1.1"><path d="M2 1h3l1 3-2 1a7 7 0 0 0 3 3l1-2 3 1v3c-6 1-10-3-9-9z"/></svg>555-014-2290</span>
    <span class="footer__item"><svg width="12" height="12" viewBox="0 0 12 12" fill="none" stroke="#6f8cff" stroke-width="1"><circle cx="6" cy="6" r="5"/><ellipse cx="6" cy="6" rx="2.2" ry="5"/><path d="M1 6h10"/></svg>WWW.HALVARDCOMPUTE.EXAMPLE</span>
  </footer>
</section>

</body>
</html>
```